Flyer Design Project

We need a flyer and teaser image designed for a March promotional campaign. We have a previous design that just needs a little refresh.
Flyer: the content of the flyer is mostly the same as the pdf you'll see on this link (http://www.quillbrookmedia.com/Digest_Pricing.pdf).
Here are the changes: change June to March, change 2011 to 2012, and remove the address of the bottom. I want the color scheme to be consistent with images I attached called "2011 teaser". I need a pdf file.
Teaser Image: the content of the teaser image is the same as "2011 teaser" image I have attached. All that needs to be changed is the month from "June" to "March". I need this to be a .jpg file that's 600x600 pixels.
Please let me know if you have any questions.
Thanks

```html
<!DOCTYPE html>
<html lang="en">
<head>
<meta charset="utf-8">
<title>Digests – March 2012 Pricing</title>
<link rel="stylesheet" href="https://fonts.googleapis.com/css2?family=Alfa+Slab+One&family=Lobster&family=Open+Sans:wght@400;700&family=Tinos&display=swap">
<style>
  :root{
    --frame:#3f8499;
    --frame-light:#4f9fb8;
    --panel-top:#e8f8fb;
    --panel-bottom:#a8cad7;
    --lime:#c8e06a;
    --red:#e53b2a;
    --orange:#f7941d;
    --bar-green:#c5d86d;
    --list-bg:#d8e5eb;
    --ink:#111;
    --sunday:#d2892c;
    --cal-green:#9dc548;
  }
  *{box-sizing:border-box;margin:0;padding:0}
  html,body{width:848px;height:1200px;overflow:hidden}
  body{background:linear-gradient(135deg,var(--frame),var(--frame-light));position:relative;font-family:"Tinos",serif;color:var(--ink)}
  .panel{position:absolute;left:21px;top:19px;width:804px;height:1158px;
    background:linear-gradient(160deg,var(--panel-top),#c9e2ea 60%,var(--panel-bottom))}
  .title{position:absolute;left:0;width:848px;text-align:center;font-family:"Alfa Slab One",serif;
    font-size:64px;top:76px;color:var(--lime);-webkit-text-stroke:2px var(--red);letter-spacing:1px}
  .subtitle{position:absolute;left:0;width:848px;text-align:center;font-family:"Lobster",cursive;
    font-size:27px;top:152px;color:var(--red);-webkit-text-stroke:1px var(--lime);font-weight:700}
  .calendar{position:absolute;left:39px;top:244px;width:366px;border-collapse:collapse;
    font-family:"Open Sans",sans-serif;background:#fff0}
  .calendar .month{background:var(--cal-green);color:#fff;font-size:13px;font-weight:700;height:17px;
    text-align:center;letter-spacing:1px;border:1px solid #444}
  .calendar .days th{font-size:6.5px;font-weight:400;height:17px;border:1px solid #444;width:52px}
  .calendar .days th.sun{font-weight:700}
  .calendar td{border:1px solid #444;height:49px;vertical-align:top;text-align:center;
    font-size:23px;font-weight:700;padding-top:6px}
  .calendar td.sun{color:var(--sunday)}
  .details{position:absolute;left:432px;top:244px;width:380px;font-size:17.5px;line-height:24px}
  .details p{margin-bottom:24px}
  .pricing-title{position:absolute;left:0;width:848px;text-align:center;top:566px;
    font-family:"Lobster",cursive;font-size:52px;color:var(--lime);-webkit-text-stroke:2px var(--red)}
  .price-board{position:absolute;left:58px;top:650px;width:735px;height:299px;background:var(--orange)}
  .size-label{position:absolute;top:26px;font-size:32px}
  .table-head{position:absolute;top:89px;height:48px;background:var(--bar-green);font-size:27px;
    display:flex;justify-content:space-between;align-items:center;padding:0 36px 0 10px}
  .table-body{position:absolute;top:137px;height:154px;background:var(--list-bg);font-size:28px;
    line-height:36px;padding:6px 0 0 12px;list-style:none}
  .col-16{left:8px;width:340px}
  .col-32{left:379px;width:347px}
  .contact{position:absolute;left:0;width:848px;text-align:center;top:1052px;font-size:17px;line-height:24px}
  .books-art{position:absolute;left:636px;top:1002px;width:191px;height:143px;border-radius:10px;
    background:linear-gradient(160deg,#b8413e,#c9803d 50%,#5b6aa8)}
</style>
</head>
<body>
<div class="panel"></div>
<h1 class="title">DIGESTS</h1>
<p class="subtitle">16 Or 32 pages / 5.5*8.5 Digest</p>

<table class="calendar">
  <tr><th class="month" colspan="7">MARCH 2012</th></tr>
  <tr class="days"><th>MONDAY</th><th>TUESDAY</th><th>WEDNESDAY</th><th>THURSDAY</th><th>FRIDAY</th><th>SATURDAY</th><th class="sun">SUNDAY</th></tr>
  <tr><td></td><td></td><td></td><td>1</td><td>2</td><td>3</td><td class="sun">4</td></tr>
  <tr><td>5</td><td>6</td><td>7</td><td>8</td><td>9</td><td>10</td><td class="sun">11</td></tr>
  <tr><td>12</td><td>13</td><td>14</td><td>15</td><td>16</td><td>17</td><td class="sun">18</td></tr>
  <tr><td>19</td><td>20</td><td>21</td><td>22</td><td>23</td><td>24</td><td class="sun">25</td></tr>
  <tr><td>26</td><td>27</td><td>28</td><td>29</td><td>30</td><td>31</td><td></td></tr>
</table>

<div class="details">
  <p>Submit your art and order by 3:00 pm EST any business day in March to take advantage of this special pricing.</p>
  <p>Each 16 or 32–page digest includes 70# gloss paper throughout, bleeds and saddle–stitching.</p>
  <p>Your directory will be delivered within 12 business days.</p>
  <p>Note: Although your order may deliver sooner, we cannot accept early delivery requests.</p>
</div>

<h2 class="pricing-title">Pricing</h2>

<section class="price-board">
  <h3 class="size-label" style="left:107px;font-weight:400">16 Pages</h3>
  <h3 class="size-label" style="left:483px;font-weight:400">32 Pages</h3>
  <div class="table-head col-16"><span>Quantity</span><span>Price</span></div>
  <div class="table-head col-32"><span>Quantity</span><span>Price</span></div>
  <ul class="table-body col-16">
    <li>5,000 ................$1,164.10</li>
    <li>10,000 ..............$1,446.40</li>
    <li>15,000 ..............$1,803.41</li>
    <li>20,000 ..............$2,148.79</li>
  </ul>
  <ul class="table-body col-32">
    <li>5,000 ................$1,999.52</li>
    <li>10,000 ..............$2,529.50</li>
    <li>15,000 ..............$3,173.53</li>
    <li>20,000 ..............$3,797.09</li>
  </ul>
</section>

<footer class="contact">
  800-555-0142 / 317-555-0186 / f 419-555-0123<br>
  www.quillbrookmedia.com
</footer>

<div class="books-art" role="img" aria-label="Illustration of a stack of colourful books with a bookmark"></div>
</body>
</html>
```